High School Hockey Player Banners

I have 22 players that i need cropped out and added to a background with the school logo, player names and player numbers. I have uploaded all players photos w/ names and number on each file name. i have uploaded the Stone Creek Hornets school logo as well as an example of something that i like to give you inspiration. The finish size is 24" tall and 18" wide

```html
<!DOCTYPE html>
<html lang="en">
<head>
<meta charset="UTF-8">
<title>Callum Brenner #17 – Stone Creek Hornets Player Banner</title>
<link href="https://fonts.googleapis.com/css2?family=Oswald:wght@300;500;700&family=Alfa+Slab+One&display=swap" rel="stylesheet">
<style>
  :root {
    --ink: #060606;
    --smoke: #1e1e1e;
    --grime: rgba(120, 92, 30, 0.35);
    --amber: #f29a0c;
    --amber-light: #f8b23a;
    --gold: #fdc10c;
    --name-gold: #fcc52e;
    --red: #c4100d;
    --white: #ffffff;
  }
  * { margin: 0; padding: 0; box-sizing: border-box; }
  html, body {
    width: 900px;
    height: 1200px;
    overflow: hidden;
    background: var(--ink);
  }
  .banner {
    position: relative;
    width: 900px;
    height: 1200px;
    overflow: hidden;
    font-family: "Oswald", sans-serif;
  }
  .panel-dark {
    position: absolute;
    left: 0; top: 0;
    width: 495px; height: 1200px;
    background:
      radial-gradient(ellipse 260px 420px at 40px 780px, var(--grime) 0%, transparent 70%),
      radial-gradient(ellipse 220px 160px at 380px 60px, rgba(120, 92, 30, 0.22) 0%, transparent 70%),
      radial-gradient(ellipse at 30% 25%, var(--smoke) 0%, var(--ink) 60%);
  }
  .panel-amber {
    position: absolute;
    left: 495px; top: 0;
    width: 405px; height: 1200px;
    background:
      radial-gradient(ellipse 200px 300px at 300px 500px, rgba(255, 210, 120, 0.35) 0%, transparent 70%),
      linear-gradient(160deg, var(--amber) 0%, var(--amber-light) 55%, var(--amber) 100%);
  }
  .name-echo {
    position: absolute;
    left: 0; top: 0;
  }
  .player-photo {
    position: absolute;
    left: 204px; top: 118px;
    width: 514px; height: 912px;
    border-radius: 120px 120px 24px 24px;
    background: linear-gradient(180deg,
      #c92a22 0%,
      #e8d8d2 22%,
      #f1ede9 40%,
      #e6e0da 58%,
      #3a3a3a 72%,
      #1a1a1a 86%,
      #d8d6d2 100%);
  }
  .player-name, .player-number, .gold-band {
    position: absolute;
    left: 0; top: 0;
  }
  .team-block {
    position: absolute;
    left: 368px; top: 1052px;
    width: 500px;
    color: var(--red);
    text-align: center;
  }
  .team-school {
    font-weight: 500;
    font-size: 30px;
    letter-spacing: 0.72em;
    line-height: 1;
    margin-right: -0.72em;
  }
  .team-mascot {
    margin-top: 14px;
    display: flex;
    align-items: center;
    justify-content: center;
    gap: 16px;
    font-weight: 500;
    font-size: 62px;
    line-height: 1;
    letter-spacing: 0.06em;
  }
  .team-mark {
    width: 40px; height: 40px;
    border-radius: 50%;
    background: var(--red);
  }
</style>
</head>
<body>
<div class="banner">
  <div class="panel-dark"></div>
  <div class="panel-amber"></div>

  <svg class="name-echo" width="900" height="1200" aria-hidden="true">
    <g font-family="Oswald, sans-serif" font-weight="500" font-size="108" fill="none" stroke-width="1.2">
      <text x="232" y="355" textLength="640" stroke="rgba(255,255,255,0.35)">CALLUM BRENNER</text>
      <text x="232" y="463" textLength="640" stroke="rgba(255,255,255,0.35)">CALLUM BRENNER</text>
      <text x="232" y="571" textLength="640" stroke="rgba(255,255,255,0.35)">CALLUM BRENNER</text>
      <text x="232" y="679" textLength="640" stroke="rgba(255,255,255,0.35)">CALLUM BRENNER</text>
      <text x="232" y="787" textLength="640" stroke="rgba(255,255,255,0.3)">CALLUM BRENNER</text>
      <text x="232" y="895" textLength="640" stroke="rgba(255,255,255,0.25)">CALLUM BRENNER</text>
      <text x="232" y="1003" textLength="640" stroke="rgba(255,255,255,0.2)">CALLUM BRENNER</text>
    </g>
  </svg>

  <div class="player-photo" role="img" aria-label="Cut-out action photo of the player skating in a red helmet and white, red and yellow team jersey, holding a hockey stick"></div>

  <svg class="player-name" width="900" height="1200">
    <text transform="translate(187 1024) rotate(-90)" font-family="Oswald, sans-serif" font-weight="700" font-size="138" fill="var(--name-gold)" textLength="982" lengthAdjust="spacingAndGlyphs">CALLUM BRENNER</text>
  </svg>

  <svg class="player-number" width="900" height="1200">
    <text x="662" y="238" font-family="'Alfa Slab One', serif" font-size="262" fill="var(--red)" textLength="190" lengthAdjust="spacingAndGlyphs">17</text>
  </svg>

  <svg class="gold-band" width="900" height="1200" aria-hidden="true">
    <polygon points="0,1068 240,1050 420,1030 640,970 900,902 900,1200 0,1200" fill="var(--gold)"/>
  </svg>

  <div class="team-block">
    <div class="team-school">STONE CREEK</div>
    <div class="team-mascot"><span class="team-mark"></span>HORNETS</div>
  </div>
</div>
</body>
</html>
```